Hip / Cool Business Card for Custom Accessory Company

I would like to get a 2 sided design for standard size business cards, glossy (2 inches x 3.5 inches). Can be landscape or portrait layout! The design should include our logo (attached). The card should be extremely clear that the company is Tin Lantern. Should also have our URL clear. Should also use the color scheme seen on our upcoming site, tinlantern.example. The font we use is called "hurry up." Other than that, please go-to-town. We are targeting 15-45 y.o. market, with a skew on the 20-30 crowd. We do custom and stock iPhone cases as well as Cufflinks, Winestoppers; see the website for more.
Updates

Project Deadline Extended
Reason: Extending in case the US July 4th Holiday is keeping people from working!!

Industry/Entity Type

Landscape

Requirements
Must have
• Must be clear that the website is tinlantern.example. Must be clear that custom designs are an option.
Nice to have
• images of our designs. examples of our designs.
Should not have
• hard on the eyes contrasting colors such as orange on black. green on blue. Should not have any fonts that are considered "old" like Times New Roman. But decorative fonts are fine.

```html
<!DOCTYPE html>
<html lang="en">
<head>
<meta charset="utf-8">
<title>Tin Lantern – Business Card</title>
<link rel="stylesheet" href="https://fonts.googleapis.com/css2?family=Audiowide&family=Marcellus&display=swap">
<style>
  :root {
    --page-bg: #d9dadc;
    --teal: #1aa3ad;
    --teal-deep: #138f99;
    --teal-light: #6fcdd6;
    --teal-mid: #4fbcc6;
    --teal-pale: #a9e2e7;
    --card-pale: #f2f8f9;
    --card-mist: #d9eef0;
    --ink: #111416;
    --accent-red: #d42a22;
    --white: #ffffff;
  }
  * { box-sizing: border-box; margin: 0; padding: 0; }
  html, body { width: 1200px; height: 900px; overflow: hidden; }
  body {
    background: var(--page-bg);
    font-family: "Marcellus", "Optima", sans-serif;
    color: var(--ink);
    position: relative;
  }
  .card {
    position: absolute;
    left: 285px;
    width: 630px;
    height: 360px;
    border-radius: 34px;
    overflow: hidden;
    box-shadow: 0 6px 18px rgba(0,0,0,0.18);
  }

  /* Front */
  .card--front { top: 60px; }
  .card--front .pattern {
    position: absolute; inset: 0;
    background:
      radial-gradient(ellipse at 30% 20%, rgba(255,255,255,0.35), rgba(255,255,255,0) 55%),
      radial-gradient(ellipse at 80% 85%, rgba(26,163,173,0.35), rgba(26,163,173,0) 60%),
      linear-gradient(135deg, var(--teal-pale) 0%, var(--teal-light) 50%, var(--teal-mid) 100%);
  }
  .brand {
    position: absolute;
    left: 0; right: 0; top: 118px;
    display: flex; align-items: center; justify-content: center; gap: 16px;
  }
  .brand__dot {
    width: 78px; height: 78px; border-radius: 50%;
    background: var(--teal);
    border: 4px solid var(--ink);
  }
  .brand__name {
    font-family: "Audiowide", sans-serif;
    font-size: 40px;
    color: var(--ink);
    letter-spacing: 1px;
  }
  .front-url {
    position: absolute; left: 60px; right: 0; bottom: 46px;
    text-align: center;
    font-family: "Audiowide", sans-serif;
    font-size: 20px;
    letter-spacing: 1px;
  }
  .front-url .hl { color: var(--accent-red); }

  /* Back */
  .card--back { top: 480px; }
  .card--back .pattern {
    position: absolute; inset: 0;
    background:
      radial-gradient(ellipse at 85% 15%, rgba(255,255,255,0.9), rgba(255,255,255,0) 55%),
      linear-gradient(135deg, var(--white) 0%, var(--card-pale) 45%, var(--card-mist) 100%);
  }
  .mascot-area { position: absolute; left: 0; top: 0; width: 630px; height: 360px; }
  .details {
    position: absolute;
    left: 330px; top: 40px;
    width: 280px;
  }
  .details__name {
    font-family: "Audiowide", sans-serif;
    font-weight: 400;
    font-size: 31px;
    line-height: 1;
    margin-bottom: 14px;
    white-space: nowrap;
  }
  .details__address { font-size: 14px; line-height: 1.2; margin-bottom: 14px; }
  .details__contact { font-size: 14px; line-height: 1.25; margin-bottom: 12px; }
  .details__contact .label { color: var(--accent-red); margin-right: 4px; }
  .url-block { display: inline-block; text-align: center; }
  .url-pill {
    display: block;
    background: var(--accent-red);
    color: var(--white);
    font-family: "Audiowide", sans-serif;
    font-size: 18px;
    padding: 3px 12px;
    border-radius: 6px;
    letter-spacing: 0.5px;
  }
  .tagline {
    font-family: "Audiowide", sans-serif;
    font-size: 8px;
    letter-spacing: 0.6px;
    margin-top: 8px;
  }
</style>
</head>
<body>

  <section class="card card--front">
    <div class="pattern" role="img" aria-label="Soft teal triangle mosaic pattern"></div>
    <div class="brand">
      <span class="brand__dot"></span>
      <span class="brand__name">TIN LANTERN</span>
    </div>
    <p class="front-url">WWW.<span class="hl">TINLANTERN</span>.EXAMPLE</p>
  </section>

  <section class="card card--back">
    <div class="pattern" role="img" aria-label="Faint pale triangle mosaic pattern"></div>
    <svg class="mascot-area" viewBox="0 0 630 360" role="img" aria-label="Large teal cartoon mascot character filling the left side of the card">
      <defs>
        <radialGradient id="mascotTone" cx="0.35" cy="0.55" r="0.75">
          <stop offset="0" stop-color="var(--teal-light)"/>
          <stop offset="0.55" stop-color="var(--teal)"/>
          <stop offset="1" stop-color="var(--teal-deep)"/>
        </radialGradient>
      </defs>
      <circle cx="20" cy="305" r="290" fill="url(#mascotTone)" stroke="var(--ink)" stroke-width="7"/>
    </svg>
    <div class="details">
      <h1 class="details__name">TIN LANTERN</h1>
      <p class="details__address">418B Copperfield Lane Unit 27<br>Brightwater, OR 97000</p>
      <p class="details__contact">
        <span class="label">P</span>555.014.2380<br>
        <span class="label">E</span>hello@tinlantern.example
      </p>
      <div class="url-block">
        <span class="url-pill">TINLANTERN.EXAMPLE</span>
        <p class="tagline">CUSTOM DESIGNS ARE AN OPTION</p>
      </div>
    </div>
  </section>

</body>
</html>
```